Brightwire Hollow Business cards

one side I would like my logo (uploaded) and the other side I want my details. I'm an electrician in sydney. The logo side I'm happy with just a white background and our logo in the middle.

Details for other side
24/7 Sydney Electrician
Marcus Pell
0431 587 219
marcus@brightwirehollow.com.au
brightwirehollow.com.au
icons for facebook, instagram, linked in

Industry/Entity Type

electrician

Contact Information for Business Card

company info

```html
<!DOCTYPE html>
<html lang="en">
<head>
<meta charset="utf-8">
<title>Brightwire Hollow – Business Card</title>
<link rel="stylesheet" href="https://fonts.googleapis.com/css2?family=Exo+2:ital,wght@0,600;0,700;1,600&family=Quicksand:wght@500&display=swap">
<style>
  :root {
    --brand-red: #c8202a;
    --ink: #222222;
    --ink-soft: #3a3a3a;
    --card: #f3f2ef;
    --backdrop: #e4e1dc;
    --dot: #8a8a8a;
  }
  * { margin: 0; padding: 0; box-sizing: border-box; }
  html, body {
    width: 1200px;
    height: 1054px;
    overflow: hidden;
    background: var(--backdrop);
  }
  .card {
    position: absolute;
    left: 170px;
    top: 267px;
    width: 860px;
    height: 520px;
    background: var(--card);
    border-radius: 22px;
    box-shadow: 0 2px 10px rgba(0,0,0,0.08);
  }
  .brand-mark {
    position: absolute;
    left: 20px;
    top: 36px;
    width: 410px;
    height: 460px;
    display: flex;
    align-items: center;
    justify-content: center;
    text-align: center;
    font-family: "Exo 2", sans-serif;
    font-weight: 700;
    font-size: 64px;
    line-height: 1.05;
    color: var(--brand-red);
  }
  .wordmark {
    position: absolute;
    left: 489px;
    top: 58px;
    font-family: "Exo 2", sans-serif;
    font-weight: 700;
    font-size: 40px;
    line-height: 1.05;
    color: var(--brand-red);
    letter-spacing: 1px;
  }
  .person {
    position: absolute;
    left: 489px;
    top: 198px;
  }
  .person-name {
    font-family: "Exo 2", sans-serif;
    font-weight: 600;
    font-size: 37px;
    line-height: 1.1;
    color: var(--brand-red);
  }
  .person-role {
    margin-top: 4px;
    font-family: "Quicksand", sans-serif;
    font-weight: 500;
    font-size: 21px;
    color: var(--ink);
  }
  .person-tagline {
    margin-top: 6px;
    font-family: "Exo 2", sans-serif;
    font-style: italic;
    font-weight: 600;
    font-size: 21px;
    color: var(--brand-red);
  }
  .contacts {
    position: absolute;
    left: 489px;
    top: 338px;
    list-style: none;
    font-family: "Quicksand", sans-serif;
    font-weight: 500;
    font-size: 21px;
    color: var(--ink-soft);
  }
  .contact-line {
    display: flex;
    align-items: center;
    height: 30px;
  }
  .contact-icon {
    width: 16px;
    height: 16px;
    margin-right: 14px;
    flex: none;
  }
  .contact-line.social {
    margin-top: 6px;
    color: var(--brand-red);
  }
  .social-dot {
    width: 18px;
    height: 18px;
    border-radius: 50%;
    background: var(--dot);
    margin-right: 12px;
    flex: none;
  }
</style>
</head>
<body>
  <section class="card">
    <div class="brand-mark">Brightwire<br>Hollow</div>

    <div class="wordmark">Brightwire<br>Hollow</div>

    <div class="person">
      <div class="person-name">Marcus Pell</div>
      <div class="person-role">Managing Director</div>
      <div class="person-tagline">24/7 Sydney Electrician</div>
    </div>

    <ul class="contacts">
      <li class="contact-line">
        <svg class="contact-icon" viewBox="0 0 16 16" aria-hidden="true">
          <path fill="#c8202a" d="M2 6c0-2 2-3 6-3s6 1 6 3v1h-3V5.5H5V7H2zM4 8h8l2 6H2z"/>
        </svg>
        0431 587 219
      </li>
      <li class="contact-line">
        <svg class="contact-icon" viewBox="0 0 16 16" aria-hidden="true">
          <rect x="1" y="3" width="14" height="10" fill="#c8202a"/>
          <path d="M1 3l7 6 7-6" fill="none" stroke="#f3f2ef" stroke-width="1.4"/>
        </svg>
        marcus@brightwirehollow.com.au
      </li>
      <li class="contact-line">
        <svg class="contact-icon" viewBox="0 0 16 16" aria-hidden="true">
          <circle cx="8" cy="8" r="7" fill="none" stroke="#c8202a" stroke-width="1.6"/>
          <ellipse cx="8" cy="8" rx="3" ry="7" fill="none" stroke="#c8202a" stroke-width="1.3"/>
          <path d="M1 8h14" stroke="#c8202a" stroke-width="1.3"/>
        </svg>
        brightwirehollow.com.au
      </li>
      <li class="contact-line social">
        <span class="social-dot" aria-hidden="true"></span>
        brightwirehollow_au
      </li>
    </ul>
  </section>
</body>
</html>
```